Vesk Architecture

We are a architectural design and build company working between scales 1/1000 to 1/1 we want people to understand our difference from our design experience and quality.we build hotels restourants and office spaces.Our company name is Vesk architecture to mind sustainability.

We want to write our adress phone and work spesifications on the card and we want our logo as backround.

Ps:you could find the logo adress and phone box numbers from the web:www.veskmimarlik-ornek.com

Target Market(s)

Who looks for experts.

Industry/Entity Type

Architecture

Requirements
Must have
• Design is over everything.
Should not have
• we don want it to be colorfull

```html
<!DOCTYPE html>
<html lang="tr">
<head>
<meta charset="utf-8">
<title>Vesk Mimarlık – Business Card</title>
<link rel="stylesheet" href="https://fonts.googleapis.com/css2?family=Open+Sans:wght@300;400;600;700&display=swap">
<style>
  :root {
    --page: #eef1ee;
    --blue-deep: #0c2a86;
    --blue-mid: #1644b4;
    --blue-bright: #2a64e0;
    --blue-ghost: rgba(90, 150, 235, 0.28);
    --band-grey: #e4e6ea;
    --white: #ffffff;
    --photo-warm-1: #8a7a66;
    --photo-warm-2: #4b4036;
    --photo-cool-1: #9fb2c4;
    --photo-cool-2: #5d6b78;
  }
  * { box-sizing: border-box; margin: 0; padding: 0; }
  html, body { width: 1200px; height: 720px; overflow: hidden; }
  body {
    background: var(--page);
    font-family: "Open Sans", Arial, sans-serif;
    position: relative;
  }
  .card {
    position: absolute;
    top: 211px;
    width: 540px;
    height: 298px;
    border-radius: 10px;
    overflow: hidden;
    box-shadow: 0 6px 18px rgba(0,0,0,0.18);
  }
  .card--back {
    left: 46px;
    background: radial-gradient(ellipse at 55% 50%, var(--blue-bright) 0%, var(--blue-mid) 45%, var(--blue-deep) 100%);
  }
  .card--front { left: 614px; background: var(--blue-deep); }
  .card-art { position: absolute; inset: 0; width: 100%; height: 100%; display: block; }

  .ghost-name {
    position: absolute;
    left: 38px;
    top: 10px;
    font-weight: 300;
    font-size: 250px;
    line-height: 1;
    letter-spacing: -6px;
    color: var(--blue-ghost);
    white-space: nowrap;
  }
  .wordmark { position: absolute; color: var(--white); }
  .wordmark-name {
    display: block;
    font-weight: 300;
    font-size: 58px;
    line-height: 1;
    letter-spacing: 1px;
  }
  .wordmark-sub {
    display: block;
    font-weight: 300;
    font-size: 16px;
    letter-spacing: 0.5px;
    margin-top: 4px;
  }
  .card--back .wordmark { left: 198px; top: 104px; }
  .card--front .wordmark { left: 78px; top: 108px; }

  .person {
    position: absolute;
    right: 20px;
    top: 42px;
    text-align: right;
    color: var(--white);
    font-size: 15.5px;
    line-height: 25px;
  }
  .contact {
    position: absolute;
    right: 20px;
    top: 182px;
    text-align: right;
    color: var(--white);
    font-size: 11.5px;
    line-height: 17px;
    font-style: normal;
  }
  .contact-line--strong { font-weight: 700; font-size: 12.5px; }
</style>
</head>
<body>

<section class="card card--back" aria-label="Card back">
  <span class="ghost-name" aria-hidden="true">vesk</span>
  <div class="wordmark">
    <span class="wordmark-name">vesk</span>
    <span class="wordmark-sub">MİMARLIK</span>
  </div>
</section>

<section class="card card--front" aria-label="Card front">
  <svg class="card-art" viewBox="0 0 540 298" aria-hidden="false">
    <defs>
      <radialGradient id="front-field" cx="0.55" cy="0.5" r="0.65">
        <stop offset="0" stop-color="#2a64e0"/>
        <stop offset="0.5" stop-color="#1644b4"/>
        <stop offset="1" stop-color="#0c2a86"/>
      </radialGradient>
      <linearGradient id="photo-warm" x1="0" y1="0" x2="1" y2="1">
        <stop offset="0" stop-color="#8a7a66"/>
        <stop offset="1" stop-color="#4b4036"/>
      </linearGradient>
      <linearGradient id="photo-cool" x1="0" y1="0" x2="1" y2="1">
        <stop offset="0" stop-color="#b9c9d8"/>
        <stop offset="1" stop-color="#5d6b78"/>
      </linearGradient>
      <linearGradient id="photo-dark" x1="0" y1="0" x2="1" y2="1">
        <stop offset="0" stop-color="#6c645c"/>
        <stop offset="1" stop-color="#2a2622"/>
      </linearGradient>
      <clipPath id="top-strip"><polygon points="0,18 330,18 262,83 0,83"/></clipPath>
      <clipPath id="bottom-strip"><polygon points="0,215 240,215 305,280 0,280"/></clipPath>
    </defs>

    <rect class="front-field" width="540" height="298" fill="url(#front-field)"/>

    <polygon class="band band--top" points="330,0 540,0 540,18 312,18" fill="#e4e6ea"/>
    <polygon class="band band--bottom" points="0,280 305,280 323,298 0,298" fill="#e4e6ea"/>

    <g class="photo-strip photo-strip--top" clip-path="url(#top-strip)">
      <rect role="img" aria-label="Photo of a bright interior with pale curtains" x="0" y="18" width="65" height="65" fill="url(#photo-cool)"/>
      <rect role="img" aria-label="Photo of a restaurant dining room" x="65" y="18" width="127" height="65" fill="url(#photo-warm)"/>
      <rect role="img" aria-label="Photo of a restaurant with ceiling lights" x="192" y="18" width="140" height="65" fill="url(#photo-dark)"/>
    </g>

    <g class="photo-strip photo-strip--bottom" clip-path="url(#bottom-strip)">
      <rect role="img" aria-label="Photo of a brick apartment building" x="0" y="215" width="68" height="65" fill="url(#photo-warm)"/>
      <rect role="img" aria-label="Photo of a modern hotel lobby" x="68" y="215" width="130" height="65" fill="url(#photo-dark)"/>
      <rect role="img" aria-label="Photo of a hotel bedroom" x="198" y="215" width="110" height="65" fill="url(#photo-cool)"/>
    </g>
  </svg>

  <div class="person">
    <p class="person-name">Deniz Arda KAYA - Mimar</p>
    <p class="person-title">Architect</p>
  </div>

  <div class="wordmark">
    <span class="wordmark-name">vesk</span>
    <span class="wordmark-sub">MİMARLIK</span>
  </div>

  <address class="contact">
    <p class="contact-line">Ihlamur Mah. Sahil Cad. Defne Sok.</p>
    <p class="contact-line">No : 7 Besiktas / ISTANBUL</p>
    <p class="contact-line contact-line--strong">t. 0212 555 01 40</p>
    <p class="contact-line contact-line--strong">f. 0212 555 01 41</p>
    <p class="contact-line">info@veskmimarlik-ornek.com</p>
  </address>
</section>

</body>
</html>
```